Tandrel Business Card

We require a professional practical business card design

Target Market(s)

Medical Professionals

Industry/Entity Type

Finance

Contact Information for Business Card

Name
Title : Finance Consultant
Qualifications : Dip Finance and Mortgage Broking Management
Membership : LBRG
Address : 3/17 Pellam Court, Yarrow Heights WA 6102
Provision for PO Box address
Provision for mobile number
Email address
Web address : www.tandrelfinance.com.au

Font styles to use
Serif

Colors
333333
9d9d9d
0355a3

Requirements
Must have
• Professional presentation

```html
<!DOCTYPE html>
<html lang="en">
<head>
<meta charset="utf-8">
<title>Tandrel Finance – Business Card</title>
<link href="https://fonts.googleapis.com/css2?family=Crimson+Text:wght@400;600;700&display=swap" rel="stylesheet">
<style>
  :root {
    --ink: #333333;
    --slate: #3b3b3b;
    --grey: #9d9d9d;
    --blue: #0355a3;
    --sky: #4fb6de;
    --paper: #ffffff;
    --stage: #dcdcdc;
  }
  * { margin: 0; padding: 0; box-sizing: border-box; }
  html, body { width: 1200px; height: 660px; overflow: hidden; }
  body {
    background: var(--stage);
    font-family: "Crimson Text", Georgia, serif;
    color: var(--ink);
    position: relative;
  }
  .card {
    position: absolute;
    top: 175px;
    width: 540px;
    height: 310px;
    box-shadow: 0 6px 18px rgba(0,0,0,.25);
    overflow: hidden;
  }
  .card-front { left: 40px; background: var(--slate); }
  .card-back  { left: 620px; background: var(--paper); }

  .brand { position: absolute; display: flex; align-items: center; gap: 12px; }
  .brand-dot { width: 46px; height: 46px; border-radius: 50%; background: var(--sky); }
  .brand-name { font-size: 40px; font-weight: 600; line-height: 1; }
  .card-front .brand { left: 50%; top: 50%; transform: translate(-50%, -50%); }
  .card-front .brand-name { color: var(--paper); }
  .card-back .brand { left: 40px; top: 112px; }
  .card-back .brand-dot { width: 58px; height: 58px; }
  .card-back .brand-name { color: var(--ink); font-size: 44px; }

  .accent-strip {
    position: absolute; right: 0; top: 18px;
    width: 14px; height: 72px; background: var(--sky);
  }
  .identity {
    position: absolute; right: 40px; top: 22px;
    text-align: right; line-height: 1.15;
  }
  .identity .person { font-size: 21px; font-weight: 700; }
  .identity .detail { font-size: 13.5px; font-weight: 600; }

  .band { position: absolute; inset: 0; }

  .address {
    position: absolute; right: 28px; top: 150px;
    color: var(--paper); font-size: 14.5px; line-height: 1.25;
    display: flex; gap: 6px; text-align: left;
  }
  .contacts {
    position: absolute; left: 22px; bottom: 14px;
    list-style: none; color: var(--paper); font-size: 14px; line-height: 1.55;
  }
  .contacts li { display: flex; align-items: center; gap: 8px; }
  .icon { width: 13px; height: 13px; flex: none; }
</style>
</head>
<body>

<section class="card card-front" aria-label="Card front">
  <div class="brand">
    <span class="brand-dot"></span>
    <span class="brand-name">Tandrel</span>
  </div>
</section>

<section class="card card-back" aria-label="Card back">
  <div class="accent-strip"></div>
  <div class="identity">
    <p class="person">Your Name</p>
    <p class="detail">Finance Consultant</p>
    <p class="detail">Dip Finance and Mortgage</p>
    <p class="detail">Broking Management</p>
    <p class="detail">LBRG</p>
  </div>

  <div class="brand">
    <span class="brand-dot"></span>
    <span class="brand-name">Tandrel</span>
  </div>

  <svg class="band" viewBox="0 0 540 310" preserveAspectRatio="none">
    <polygon points="0,232 540,120 540,310 0,310" fill="var(--slate)"/>
    <line x1="0" y1="232" x2="540" y2="120" stroke="var(--sky)" stroke-width="4"/>
  </svg>

  <div class="address">
    <svg class="icon" viewBox="0 0 12 16"><path d="M6 0a6 6 0 0 1 6 6c0 4-6 10-6 10S0 10 0 6a6 6 0 0 1 6-6z" fill="var(--sky)"/><circle cx="6" cy="6" r="2.2" fill="var(--slate)"/></svg>
    <span>3/17 Pellam Court<br>Yarrow Heights WA 6102</span>
  </div>

  <ul class="contacts">
    <li><svg class="icon" viewBox="0 0 12 16"><rect x="1" y="0" width="10" height="16" rx="2" fill="var(--sky)"/><rect x="3" y="2" width="6" height="10" fill="var(--slate)"/></svg>0400 555 218</li>
    <li><svg class="icon" viewBox="0 0 16 12"><rect width="16" height="12" rx="1" fill="var(--sky)"/><path d="M1 1l7 6 7-6" stroke="var(--slate)" stroke-width="1.5" fill="none"/></svg>enquiries@tandrelfinance.com.au</li>
    <li><svg class="icon" viewBox="0 0 16 16"><circle cx="8" cy="8" r="7.5" fill="var(--sky)"/><path d="M0.5 8h15M8 0.5c-4 4-4 11 0 15M8 0.5c4 4 4 11 0 15" stroke="var(--slate)" stroke-width="1.2" fill="none"/></svg>www.tandrelfinance.com.au</li>
  </ul>
</section>

</body>
</html>
```